Real Estate Team Needs Business Cards

Double sided - Team Member on Front, Team Leader on Back (back side will contain more details).
Colors to use:
Red = R: 233 G: 1 B: 2
Grey = R: 89 G: 89 B: 89
Black= R: 0 B: 0 B: 0
** MAIN FOCUS ** ( separate border, color, design, etc. to really stand out - whatever you think draws the most attention ) on both sides for "Sell for 1%‡" and "Buy & receive up to a 1% rebate‡". Must have fine print **
**Please make both sides stand out and look unique / different
Business card to have round corners (standard size 3.5" x 2").:
Document Trim Size
89 x 51 mm
1050 x 600 pixels
Full Bleed Size
92 x 54 mm
1085 x 635 pixels
Basic example provided. Please redesign as you see best. In your design - Please use the same picture on both sides. Name, address, phone number, email, etc. will be provided to the selected design. QR code on back side only if there is room (not important)

```html
<!DOCTYPE html>
<html lang="en">
<head>
<meta charset="utf-8">
<title>Keystone Harbor Realty – Business Cards</title>
<link href="https://fonts.googleapis.com/css2?family=Alegreya:ital,wght@1,400&family=Arimo:wght@400;700&display=swap" rel="stylesheet">
<style>
  :root {
    --red: #e90102;
    --grey: #595959;
    --black: #000000;
    --peach: #f6c3b0;
    --white: #ffffff;
    --backdrop: #cbcbcb;
    --navy: #1f3f86;
  }
  * { box-sizing: border-box; margin: 0; padding: 0; }
  html, body { width: 1125px; height: 1200px; overflow: hidden; }
  body {
    background: var(--backdrop);
    font-family: "Arimo", Arial, sans-serif;
    color: var(--grey);
    position: relative;
  }
  .card {
    position: absolute;
    left: 178px;
    width: 768px;
    height: 436px;
    background: var(--white);
    border-radius: 24px;
    overflow: hidden;
    box-shadow: 0 4px 8px rgba(0,0,0,0.25);
  }
  .card--front { top: 140px; }
  .card--back { top: 626px; }

  .brand {
    position: absolute;
    display: flex;
    align-items: center;
    gap: 10px;
    font-weight: 700;
    font-size: 25px;
    letter-spacing: 0.5px;
    color: var(--black);
    white-space: nowrap;
  }
  .brand__square { width: 22px; height: 22px; background: var(--red); flex: none; }
  .card--front .brand { left: 30px; top: 88px; }
  .card--back .brand { right: 68px; top: 78px; }

  .offer-band {
    position: absolute;
    left: 0; width: 100%;
    height: 43px;
    display: flex;
    align-items: center;
    font-family: "Alegreya", Georgia, serif;
    font-style: italic;
    font-size: 24px;
    color: var(--white);
    white-space: nowrap;
  }
  .card--front .offer-band {
    top: 158px;
    padding-left: 30px;
    background: linear-gradient(90deg, var(--red) 0%, var(--red) 55%, #ee6a4a 78%, var(--peach) 100%);
  }
  .card--back .offer-band {
    top: 132px;
    justify-content: flex-end;
    padding-right: 21px;
    background: linear-gradient(90deg, var(--peach) 0%, #ee6a4a 24%, var(--red) 45%, var(--red) 100%);
  }

  .portrait {
    position: absolute;
    bottom: 0;
    width: 276px;
    height: 380px;
    background: linear-gradient(180deg, #e9d3c6 0%, #e4c6b5 38%, #f3f3f3 52%, #33549c 64%, var(--navy) 100%);
    border-radius: 120px 120px 0 0;
  }
  .card--front .portrait { right: 0; }
  .card--back .portrait { left: 0; }

  .person__name {
    color: var(--red);
    font-weight: 700;
    font-size: 24px;
    line-height: 1;
  }
  .person__role { font-size: 18px; margin-top: 6px; }
  .person__rule { width: 12px; height: 3px; background: var(--black); margin: 10px 0 12px; }
  .contact-list { list-style: none; }
  .contact-list li {
    display: flex;
    align-items: center;
    gap: 8px;
    font-size: 18px;
    line-height: 24px;
  }
  .contact-list svg { width: 12px; height: 12px; flex: none; fill: var(--red); }

  .card--front .person { position: absolute; left: 30px; top: 243px; }
  .card--back .person { position: absolute; left: 320px; top: 239px; }
  .card--back .person__role { margin-top: 4px; }
  .person__address { font-size: 18px; margin: 17px 0 14px; }

  .services {
    position: absolute;
    top: 187px;
    left: 228px;
    display: flex;
    gap: 8px;
    list-style: none;
    font-size: 14px;
    white-space: nowrap;
  }
  .services li { display: flex; align-items: center; gap: 4px; }
  .services li::before {
    content: ""; width: 5px; height: 5px; border-radius: 50%; background: var(--red);
  }
</style>
</head>
<body>

<section class="card card--front" aria-label="Team member side">
  <div class="brand"><span class="brand__square"></span>KEYSTONE HARBOR REALTY</div>
  <div class="offer-band">Sell for 1%‡" and "Buy &amp; receive up to a 1% rebate‡</div>
  <div class="portrait" role="img" aria-label="Portrait photo of the team member in a navy suit and light blue tie"></div>
  <div class="person">
    <h2 class="person__name">Dana Whitlock</h2>
    <p class="person__role">Employee</p>
    <div class="person__rule"></div>
    <ul class="contact-list">
      <li><svg viewBox="0 0 12 12"><path d="M2.5 0.8 4.3 2.9 3.3 4.3c.7 1.6 2 2.9 3.5 3.6l1.3-1 2.2 1.8-1 1.9C5.4 10.5 1.4 6.5.6 2.4z"/></svg>555-010-4821</li>
      <li><svg viewBox="0 0 12 12"><path d="M3 0h6v12H3zM4 1.2v8.4h4V1.2zM5.3 10.3h1.4v.9H5.3z"/></svg>555-014-77365</li>
      <li><svg viewBox="0 0 12 12"><path d="M0 2h12v8H0zM1 3.2v.3l5 3.2 5-3.2v-.3z"/></svg>hello@keystoneharborrealty.com</li>
      <li><svg viewBox="0 0 12 12"><path d="M6 0a6 6 0 1 0 0 12A6 6 0 0 0 6 0zM3 2.5c1 0 2 .6 2.2 1.5L4 5.5l.6 1.6-1.2 1.5L2 5.8 1.8 3.6zM8.2 6.2l1.6.8-.6 2.3-1.7.9-.4-2.2z"/></svg>www.keystoneharborrealty.com</li>
    </ul>
  </div>
</section>

<section class="card card--back" aria-label="Team leader side">
  <div class="portrait" role="img" aria-label="Portrait photo of the team leader in a navy suit and light blue tie"></div>
  <div class="brand"><span class="brand__square"></span>KEYSTONE HARBOR REALTY</div>
  <div class="offer-band">Sell for 1%‡" and "Buy &amp; receive up to a 1% rebate‡</div>
  <ul class="services">
    <li>Free Home Evaluation</li>
    <li>Free Local Sold Reports</li>
    <li>Advanced Property Search</li>
  </ul>
  <div class="person">
    <h2 class="person__name">Marcus Ellery</h2>
    <p class="person__role">Owner</p>
    <p class="person__address">418 Linden Ave, IN 46010</p>
    <ul class="contact-list">
      <li><svg viewBox="0 0 12 12"><path d="M2.5 0.8 4.3 2.9 3.3 4.3c.7 1.6 2 2.9 3.5 3.6l1.3-1 2.2 1.8-1 1.9C5.4 10.5 1.4 6.5.6 2.4z"/></svg>555-010-4821</li>
      <li><svg viewBox="0 0 12 12"><path d="M0 2h12v8H0zM1 3.2v.3l5 3.2 5-3.2v-.3z"/></svg>hello@keystoneharborrealty.com</li>
      <li><svg viewBox="0 0 12 12"><path d="M6 0a6 6 0 1 0 0 12A6 6 0 0 0 6 0zM3 2.5c1 0 2 .6 2.2 1.5L4 5.5l.6 1.6-1.2 1.5L2 5.8 1.8 3.6zM8.2 6.2l1.6.8-.6 2.3-1.7.9-.4-2.2z"/></svg>www.keystoneharborrealty.com</li>
    </ul>
  </div>
</section>

</body>
</html>
```